Business Card for Veltrano, a french tech company

Tech company
New technologies
Serious design
Dark theme

User info :
Name: Mathis CORLAVE
Position: Co-Founder & CEO
Tel: (+33) 6 58 24 90 37
Email: mathis@veltrano.io
Website: www.veltrano.io
Address: 17 rue des Tanneurs 69002 LYON

Attached is the business logo file.

```html
<!DOCTYPE html>
<html lang="en">
<head>
<meta charset="utf-8">
<title>Veltrano – Business Card</title>
<link rel="stylesheet" href="https://fonts.googleapis.com/css2?family=Open+Sans:wght@400;600;700;800&display=swap">
<style>
  :root {
    --bg: #2e2e2e;
    --card: #1a1a1a;
    --brand: #8f4aae;
    --accent: #c2369f;
    --ink: #f2f2f2;
  }
  * { box-sizing: border-box; margin: 0; padding: 0; }
  html, body { width: 1200px; height: 689px; overflow: hidden; }
  body {
    background: var(--bg);
    font-family: "Open Sans", Arial, sans-serif;
    position: relative;
  }
  .card {
    position: absolute;
    top: 185px;
    width: 560px;
    height: 320px;
    background: var(--card);
    border-radius: 22px;
    box-shadow: 0 14px 34px rgba(0,0,0,.45);
  }
  .card-front { left: 30px; display: flex; align-items: center; justify-content: center; }
  .card-back { left: 610px; }

  .wordmark {
    font-weight: 800;
    color: var(--brand);
    letter-spacing: .02em;
    line-height: 1;
  }
  .card-front .wordmark { font-size: 76px; }
  .card-back .wordmark {
    position: absolute;
    left: 46px;
    top: 184px;
    font-size: 36px;
  }

  .divider {
    position: absolute;
    left: 300px;
    top: 58px;
    width: 1.5px;
    height: 200px;
    background: var(--accent);
  }
  .contact {
    position: absolute;
    left: 326px;
    top: 58px;
    color: var(--ink);
  }
  .contact-name { font-size: 22px; font-weight: 700; color: var(--accent); line-height: 1.1; }
  .contact-role { font-size: 13px; margin-top: 3px; }
  .contact-list { list-style: none; margin-top: 18px; }
  .contact-list li {
    display: flex; align-items: center; gap: 8px;
    font-size: 12.5px; line-height: 21px;
  }
  .contact-list svg { width: 12px; height: 12px; fill: var(--accent); flex: none; }
  .contact-address { font-size: 12.5px; line-height: 19px; margin-top: 16px; padding-left: 20px; }
</style>
</head>
<body>
  <section class="card card-front">
    <div class="wordmark">VELTRANO</div>
  </section>

  <section class="card card-back">
    <div class="wordmark">VELTRANO</div>
    <div class="divider"></div>
    <div class="contact">
      <p class="contact-name">Elias Varden</p>
      <p class="contact-role">Managing Director</p>
      <ul class="contact-list">
        <li>
          <svg viewBox="0 0 24 24"><path d="M6.6 10.8a15.1 15.1 0 0 0 6.6 6.6l2.2-2.2c.3-.3.7-.4 1-.2 1.1.4 2.3.6 3.6.6.6 0 1 .4 1 1V20c0 .6-.4 1-1 1A17 17 0 0 1 3 4c0-.6.4-1 1-1h3.5c.6 0 1 .4 1 1 0 1.3.2 2.5.6 3.6.1.3 0 .7-.2 1z"/></svg>
          123 456 789
        </li>
        <li>
          <svg viewBox="0 0 24 24"><path d="M2 5h20v14H2z M2 5l10 8 10-8" /><path d="M3 6l9 7 9-7v1l-9 7-9-7z" fill="#1a1a1a"/></svg>
          info@yourgmail.com
        </li>
        <li>
          <svg viewBox="0 0 24 24"><circle cx="12" cy="12" r="10"/><path d="M2 12h20M12 2c3 3 3 17 0 20M12 2c-3 3-3 17 0 20" stroke="#1a1a1a" stroke-width="1.5" fill="none"/></svg>
          www.yourwebsite.com
        </li>
      </ul>
      <p class="contact-address">Your address, City<br>State, Zip 1234</p>
    </div>
  </section>
</body>
</html>
```